Quality Monitoring Company Needs a New Site

We are an established company that has a fair number of clients but the site lacks current design standards that we'd like to keep up with. We'd like to mimic the same style of the site on quorvlinapp.example, belstrum.example, https://tindleworkpays.example/, etc. We'd also like to make sure the designer understands SEO Silos and how it effects the design elements. Attached is the structure that I'd like to follow for the pages. You don't need to design every single sub-page because they'll probably be fairly similar; however, I want to see at least 1 each. Please use the content on our current site for filler areas. Please try to do a good job of understanding what we do so you can use your best judgement on what is needed to be successful. Use our color scheme and the logo should be the side view but I included the AI just in case.
Updates

I am narrowing down on the field of designs that I have received. There are a lot of similarities between the designs I like and don't like. I'd also like to ensure that some of the inner pages get done in the next 5 days so I can see the creativity that is there as well. That is probably what is next -- getting a few inner pages completed so I can see what you can come up with (not based on our current website) because the current "front pages" are all so good and so close.

Industry/Entity Type

Telecommunications

Colors

Designer to choose colors to be used in the design.

Requirements
Must have
• SEO Silo Look and Feel
• Current Colors
Should not have
• No stockphotos whatsoever. NONE.

```html
<!DOCTYPE html>
<html lang="en">
<head>
<meta charset="utf-8">
<title>Tallyquest — Call Center Quality Assurance</title>
<link href="https://fonts.googleapis.com/css2?family=Questrial&family=Montserrat:wght@400;600&display=swap" rel="stylesheet">
<style>
:root{
  --navy:#0b3260;
  --navy-deep:#082748;
  --blue:#1ba6e1;
  --blue-mid:#1380c4;
  --ink:#1d1d1f;
  --muted:#6d7178;
  --line:#e6e8ec;
  --white:#ffffff;
  --photo-a:#9aa7b4;
  --photo-b:#5d6b78;
}
*{box-sizing:border-box;margin:0;padding:0}
html,body{width:1200px;height:4342px;overflow:hidden;background:var(--white)}
body{font-family:"Montserrat",sans-serif;color:var(--ink);position:relative}
.page{position:relative;width:1200px;height:4342px;overflow:hidden}
.abs{position:absolute}
.backdrop{position:absolute;left:0;top:0}
h1,h2,h3,h4,.display{font-family:"Questrial",sans-serif;font-weight:400}
.btn{position:absolute;display:flex;align-items:center;justify-content:center;font-family:"Questrial",sans-serif;color:var(--white);background:var(--navy);border-radius:3px;text-decoration:none}
.btn.light{background:var(--blue)}
.photo{position:absolute;border-radius:50%;border:8px solid var(--white);box-shadow:0 4px 18px rgba(0,0,0,.18);background:linear-gradient(135deg,var(--photo-a),var(--photo-b))}
.logo{position:absolute;display:flex;align-items:center;gap:12px;font-family:"Questrial",sans-serif;color:var(--white)}
.logo .dot{width:22px;height:22px;border-radius:50%;background:var(--white)}
/* header */
.nav{position:absolute;top:38px;left:672px;display:flex;gap:28px;font-size:12px;font-family:"Montserrat",sans-serif;color:var(--ink)}
.menu-icon{position:absolute;left:900px;top:34px;width:26px}
.menu-icon span{display:block;height:2px;background:var(--blue);margin-bottom:7px}
.login{left:948px;top:31px;width:90px;height:36px;font-size:13px;background:var(--navy-deep)}
/* hero */
.hero-title{position:absolute;right:162px;top:212px;text-align:right;font-size:40px;line-height:48px;color:var(--navy)}
.hero-title em{font-style:normal;color:var(--blue)}
.hero-sub{position:absolute;right:162px;top:315px;text-align:right;font-family:"Questrial",sans-serif;font-size:19px;line-height:27px;color:var(--navy)}
/* welcome */
.welcome{position:absolute;left:162px;top:778px;width:430px}
.welcome h2{font-size:35px;color:var(--ink);margin-bottom:18px}
.welcome p{font-size:11.5px;line-height:21px;color:var(--muted);margin-bottom:6px}
.welcome p.accent{color:var(--blue)}
.checks{list-style:none;font-size:11.5px;color:var(--muted);line-height:21px}
.checks li{display:flex;align-items:center;gap:8px}
.checks li::before{content:"";width:9px;height:9px;border:2px solid var(--navy);border-radius:50%}
.device{position:absolute;left:851px;top:649px;width:228px;height:472px;border-radius:34px;background:linear-gradient(180deg,var(--navy) 0 30%,#f3f5f8 30%);border:6px solid #1c1c1e}
/* services */
.section-title{position:absolute;left:0;width:1200px;text-align:center;font-size:33px;color:var(--ink)}
.card{position:absolute;width:277px;background:var(--white);border:1px solid var(--line);box-shadow:0 3px 12px rgba(0,0,0,.05);padding:54px 16px 0}
.card h3{font-size:16px;line-height:22px;color:var(--ink);margin-bottom:10px}
.card p{font-size:10.5px;line-height:19px;color:var(--muted)}
.card a{display:block;margin-top:16px;font-family:"Questrial",sans-serif;font-size:13px;color:var(--navy);text-decoration:none}
.card-icon{position:absolute;left:38px;top:-38px;width:70px;height:70px;border-radius:50%;background:var(--white);box-shadow:0 2px 10px rgba(0,0,0,.12);display:flex;align-items:center;justify-content:center}
/* hybrid */
.hybrid{position:absolute;left:162px;top:1786px;width:420px;color:var(--white)}
.hybrid h2{font-size:36px;line-height:48px;margin-bottom:30px}
.hybrid p{font-size:11.5px;line-height:21px;margin-bottom:18px}
.hybrid p strong{font-weight:600}
.screen{position:absolute;left:657px;top:1870px;width:560px;height:490px;background:linear-gradient(160deg,#d9dde2,#b3bac2);border-radius:18px}
/* needs */
.needs{position:absolute;left:337px;top:2632px;width:526px;height:165px;border:1px solid var(--line);box-shadow:0 3px 14px rgba(0,0,0,.06);text-align:center}
.needs h3{font-size:17px;color:var(--navy);padding:17px 0 13px;border-bottom:1px solid var(--line)}
.needs p{font-size:11px;line-height:20px;color:var(--muted);padding:14px 26px}
.dots{position:absolute;top:2838px;left:548px;display:flex;gap:18px}
.dots span{width:12px;height:12px;border-radius:50%;background:#cfd6df}
.dots span:first-child{background:var(--navy)}
/* blog */
.post{position:absolute;top:2996px;width:277px;height:231px;background:var(--white);border:1px solid var(--line);box-shadow:0 3px 14px rgba(0,0,0,.06);padding:10px}
.post .thumb{height:150px;background:linear-gradient(135deg,#c9cfd6,#7d8894)}
.post h4{font-size:13.5px;color:var(--ink);margin-top:14px}
.post time{display:block;font-family:"Questrial",sans-serif;font-size:11px;color:var(--blue);margin-top:4px}
/* proof */
.proof{position:absolute;left:612px;top:3425px;width:420px}
.proof h2{font-size:36px;color:var(--ink);margin-bottom:14px}
.proof p{font-size:11.5px;line-height:21px;color:var(--muted);margin-bottom:4px}
.video{position:absolute;left:76px;top:3472px;width:336px;height:336px;border-radius:50%;border:8px solid var(--white);background:radial-gradient(circle,#3a4350,#161b22);box-shadow:0 4px 18px rgba(0,0,0,.2)}
/* footer */
.help{position:absolute;left:0;width:1650px;text-align:center;color:var(--white)}
.foot-col{position:absolute;top:4080px;color:var(--white)}
.foot-col h4{font-size:15px;margin-bottom:22px}
.foot-col ul{list-style:none;font-size:11px;line-height:21px}
.foot-about{position:absolute;left:180px;top:4110px;width:240px;text-align:center;color:var(--white);font-size:11px;line-height:21px}
.socials{position:absolute;left:200px;top:4220px;display:flex;gap:16px}
.socials span{width:36px;height:36px;border:2px solid var(--white);border-radius:50%}
.contact-row{display:flex;gap:14px;align-items:flex-start;font-size:11px;line-height:20px;margin-bottom:22px}
.copyright{position:absolute;left:0;top:4297px;width:1200px;height:45px;background:var(--navy-deep);color:var(--white);font-size:12px;display:flex;align-items:center;justify-content:center}
</style>
</head>
<body>
<div class="page">

<svg class="backdrop" width="1200" height="4342" viewBox="0 0 1200 4342" aria-hidden="true">
  <defs>
    <linearGradient id="g-hero" x1="0" y1="1" x2="1" y2="0">
      <stop offset="0" stop-color="#082748"/><stop offset=".55" stop-color="#0c4f8c"/><stop offset="1" stop-color="#1ba6e1"/>
    </linearGradient>
    <linearGradient id="g-wave" x1="0" y1="0" x2="1" y2="1">
      <stop offset="0" stop-color="#1ba6e1"/><stop offset=".6" stop-color="#1380c4"/><stop offset="1" stop-color="#0b3260"/>
    </linearGradient>
    <linearGradient id="g-foot" x1="0" y1="1" x2="1" y2="0">
      <stop offset="0" stop-color="#0b3260"/><stop offset=".6" stop-color="#1380c4"/><stop offset="1" stop-color="#1ba6e1"/>
    </linearGradient>
  </defs>
  <path d="M0 0H930C870 140 660 150 540 270C420 390 360 700 0 785Z" fill="url(#g-hero)"/>
  <path d="M1200 560C1070 600 1000 700 985 850C970 1000 1060 1080 1200 1090Z" fill="url(#g-hero)"/>
  <path d="M0 1735C180 1690 300 1640 430 1700C560 1760 580 1860 720 1880C870 1900 980 1790 1200 1830V2560C1150 2490 1060 2410 950 2360C800 2300 600 2290 400 2320C250 2340 100 2360 0 2345Z" fill="url(#g-wave)"/>
  <path d="M0 3310C160 3318 380 3345 400 3500C420 3700 250 3820 0 3862Z" fill="url(#g-wave)"/>
  <path d="M0 4000C300 3950 520 3960 710 3820C860 3720 1050 3740 1200 3700V4342H0Z" fill="url(#g-foot)"/>
  <line x1="458" y1="4044" x2="1035" y2="4044" stroke="#ffffff" stroke-opacity=".35"/>
</svg>

<!-- header -->
<div class="logo" style="left:162px;top:18px;font-size:54px"><span class="dot"></span>Tallyquest</div>
<nav class="nav"><span>Home</span><span>Services</span><span>Contact Us</span></nav>
<div class="menu-icon"><span></span><span></span><span></span></div>
<a class="btn login">Login Us</a>

<!-- hero -->
<div class="photo" role="img" aria-label="Photo of two colleagues meeting at a desk" style="left:112px;top:168px;width:410px;height:410px"></div>
<div class="photo" role="img" aria-label="Photo of a hand holding a payment card" style="left:390px;top:565px;width:146px;height:146px;border-width:6px"></div>
<h1 class="hero-title">When was the last time<br><em>Vexa delighted</em></h1>
<p class="hero-sub">you with a satisfying and surprising<br>answer or action?</p>
<a class="btn" style="left:657px;top:409px;width:179px;height:51px;font-size:19px">Free A Quote</a>
<a class="btn light" style="left:859px;top:409px;width:180px;height:51px;font-size:19px">Explore More</a>

<!-- welcome -->
<section class="welcome">
  <h2>Welcome to Tallyquest</h2>
  <p>We are an affordable, accurate, and fully scalable Call Center Quality Assurance Agency. Tallyquest is born of the innate understanding that accurate and scalable Third Party Call Center QA services are paramount to boosting efficiency, profitability, and growth.</p>
  <p class="accent">Unfortunately, for many QA services, Call Center Quality Assurance is best summarized as one of three options:</p>
  <ul class="checks">
    <li>Relying solely on inaccurate voice-to-text technologies</li>
    <li>Hiring expensive and specialized in-house QA teams</li>
    <li>Busy team leaders and supervisors doing agent performance reviews</li>
  </ul>
</section>
<a class="btn" style="left:162px;top:1081px;width:120px;height:39px;font-size:13px">Read More</a>
<div class="device" role="img" aria-label="Phone screen showing the quality dashboard app"></div>
<div class="photo" role="img" aria-label="Photo of a team reviewing work together" style="left:729px;top:920px;width:176px;height:176px"></div>
<div class="photo" role="img" aria-label="Photo of an agent on a call" style="left:1124px;top:572px;width:120px;height:120px;border-width:6px"></div>

<!-- services -->
<h2 class="section-title" style="top:1185px">Quality Assurance Services</h2>
<article class="card" style="left:162px;top:1323px;height:231px">
  <div class="card-icon"><svg width="40" height="40" viewBox="0 0 40 40" fill="none" stroke="#0b3260" stroke-width="2"><rect x="4" y="6" width="32" height="30"/><path d="M10 30v-6M16 30v-10M22 30v-8M28 30v-14M8 18l8-6 6 4 10-8"/></svg></div>
  <h3>Evaluating and Scoring Agent-customer Interactions</h3>
  <p>Which of your agents have performance issues and why? Tallyquest's highly dynamic algorithms can identify key strengths.</p>
  <a>Discover More</a>
</article>
<article class="card" style="left:460px;top:1390px;height:231px">
  <div class="card-icon"><svg width="40" height="40" viewBox="0 0 40 40" fill="none" stroke="#0b3260" stroke-width="2"><rect x="8" y="4" width="22" height="32"/><path d="M12 12h14M12 18h14M12 24h10M33 6v22"/></svg></div>
  <h3>Identifying Key Behaviors and Procedures that Drive Sales</h3>
  <p>With an excess of 25 million minutes reviewed, we have highly experienced call center quality assurance specialists to help you identify patterns and behaviors.</p>
  <a>Discover More</a>
</article>
<article class="card" style="left:762px;top:1458px;height:230px">
  <div class="card-icon"><svg width="40" height="40" viewBox="0 0 40 40" fill="none" stroke="#0b3260" stroke-width="2"><path d="M4 16l8-8 8 6 8-6 8 8-16 16z"/><path d="M14 22l4 4M18 18l5 5"/></svg></div>
  <h3>Keeping Call Centers Compliant</h3>
  <p>Organizations that have outsourced their QA program to Tallyquest have on average benefited from month over month reductions in compliance violations at a rate of 7%.</p>
  <a>Discover More</a>
</article>

<!-- hybrid -->
<section class="hybrid">
  <h2>Ushering The Era of<br>Machine-Human Hybrid</h2>
  <p>Tallyquest is committed to providing call centers of all shapes and sizes with the essential tools they need to thrive and survive in a world riddled with compliance violations and stagnant agent performance.</p>
  <p>The same collaborative approach between humans and machines that Tallyquest employs to ensure accurate, affordable and fully scalable Call Center QA services has gained traction in many other areas; from solving climate change and geopolitical conflict to Centaur chess.</p>
  <p><strong>Experience efficient, affordable and fully scalable call center QA services today.</strong></p>
</section>
<a class="btn" style="left:162px;top:2179px;width:120px;height:40px;font-size:13px">Get In Touch</a>
<div class="screen" role="img" aria-label="Illustration of a desktop monitor with a cartoon character at a desk and the words Stuck with an outdated form"></div>

<!-- needs -->
<h2 class="section-title" style="top:2557px">Call Center QA Needs?</h2>
<div class="needs">
  <h3>Affordable &amp; Cost Effective Call Center QA Services</h3>
  <p>Starting at only 20¢ per CALL minute, we are cheaper than the latest QA technologies or hiring an internal QA team. What's more, we are just as accurate, can scale easily, and provide a full call center QA solution for you to impact positive change in your call center.</p>
</div>
<div class="dots"><span></span><span></span><span></span><span></span></div>

<!-- blog -->
<h2 class="section-title" style="top:2918px">Latest Blog</h2>
<article class="post" style="left:162px"><div class="thumb" role="img" aria-label="Photo of two women talking at a table"></div><h4>7 Important Call Center Skills For Agents</h4><time>21 October 2019</time></article>
<article class="post" style="left:460px"><div class="thumb" role="img" aria-label="Photo of a team meeting in an office"></div><h4>Process vs. Product 1 Easy Solution</h4><time>19 October 2019</time></article>
<article class="post" style="left:762px"><div class="thumb" role="img" aria-label="Photo of a man working on a laptop on the floor"></div><h4>Call Center Coaching For 2020</h4><time>13 October 2019</time></article>
<a class="btn" style="left:539px;top:3277px;width:121px;height:39px;font-size:13px">Explore More</a>

<!-- proof -->
<div class="video" role="img" aria-label="Video still of a call center operations room">
  <svg class="abs" style="left:134px;top:134px" width="52" height="52" viewBox="0 0 52 52" fill="none" stroke="#fff" stroke-width="3"><circle cx="26" cy="26" r="23"/><path d="M21 16l14 10-14 10z" fill="#fff"/></svg>
</div>
<div class="photo" role="img" aria-label="Photo of a man on the phone" style="left:320px;top:3346px;width:142px;height:142px;border-width:6px"></div>
<section class="proof">
  <h2>Proof of Our Value</h2>
  <p>Organizations that have outsourced their QA program to Tallyquest experienced reductions in compliance violation at a rate of 7%, increased lead conversions at a rate of 12% while improving customer retention at a rate of 9%.</p>
  <p>Call us today for a consultation on your call center's current performance and ideas how to get better performance from your team.</p>
</section>
<a class="btn" style="left:612px;top:3645px;width:111px;height:40px;font-size:13px">More Info</a>

<!-- footer -->
<svg class="abs" style="left:796px;top:3808px" width="60" height="60" viewBox="0 0 60 60"><circle cx="30" cy="30" r="28" fill="#fff"/><circle cx="30" cy="30" r="22" fill="none" stroke="#1ba6e1" stroke-width="1.5" stroke-dasharray="3 3"/><path d="M23 21c2-2 4 0 5 2s-1 3-1 4 3 5 5 5 2-3 4-1 2 4 0 5c-6 3-17-8-13-15z" fill="#0b3260"/></svg>
<div class="help display" style="top:3884px;left:0;width:1650px;font-size:19px">Need Help? Give us a call</div>
<div class="help" style="top:3912px;font-size:11px">Don't Hesitate call us now to know More about us</div>
<div class="help display" style="top:3938px;font-size:31px">(800-555-0142 )</div>

<div class="logo" style="left:216px;top:4040px;font-size:34px"><span class="dot" style="width:16px;height:16px"></span>Tallyquest</div>
<p class="foot-about">We are an affordable, accurate, and fully scalable Call Center Quality Assurance Agency. Tallyquest is born of the innate understanding that accurate and scalable.</p>
<div class="socials"><span></span><span></span><span></span><span></span></div>

<div class="foot-col" style="left:470px"><h4>Resources</h4><ul><li>Team</li><li>FAQ</li><li>Terms &amp; Agreements</li><li>Blog</li><li>In the News</li><li>Location</li></ul></div>
<div class="foot-col" style="left:672px"><h4>Company</h4><ul><li>Home</li><li>Services</li><li>System Details</li><li>Sample Score Cards</li><li>Pricing</li><li>Contact Us</li></ul></div>
<div class="foot-col" style="left:874px"><h4>Contact Info</h4>
  <div class="contact-row"><svg width="18" height="24" viewBox="0 0 18 24"><path d="M9 1a8 8 0 0 1 8 8c0 6-8 14-8 14S1 15 1 9a8 8 0 0 1 8-8z" fill="none" stroke="#fff" stroke-width="2"/><circle cx="9" cy="9" r="3" fill="#fff"/></svg><span>4410 Harbor Lane,<br>Eastfield, CA 90000</span></div>
  <div class="contact-row"><svg width="20" height="14" viewBox="0 0 20 14"><rect x="1" y="1" width="18" height="12" fill="none" stroke="#fff" stroke-width="2"/><path d="M1 1l9 7 9-7" fill="none" stroke="#fff" stroke-width="2"/></svg><span>Hello(at)Tallyquest.example</span></div>
</div>

<div class="copyright">Copyright-2019 © Tallyquest. Terms &amp; Conditonds | Privacy Policy.</div>
</div>
</body>
</html>
```